Build our new website pages and templates

BACKGROUND
• We are migrating over from an old website and URL ( www.plotmarker.co.nz ) to a brand new website with a new URL – www.halvoro.co.nz
• We have already selected a logo for the new website – see attached.
• We manage all our websites in house using Dreamweaver and want to retain the capability of doing this for the new site.

-------------------------------------------------------------------------------------

BRIEF
• Design the new look halvoro website for our company including color palette, fonts, icons, graphics and layout.

• The design should reflect our high quality venue hire services to corporate buyers, picking up inspiration from our beautiful new logo

• The index page should also incorporate our:

o What We Do page
o How To Use Our Site page
o Are you a venue? content (with link to the 'List A Venue' page)
o Our key contact links
o Our navigation menu

Here are some examples of the types of Index pages that appeal to us:

http://brightpebblelane.com/
What we like about it: Like the simplicity of the page and the scroll function to show different page elements.

http://www.trelbo.com/
What we like about it: Strong blocks of hero images and fonts. Easy scroll from one section to the next.

https://www.lumz.com/
What we like about it: Like the scroll feature to different sections.

https://www.plankhub.net/
What we like about it: Simple stylish Index page that scrolls easily

Our version would be:
1. Our logo centre page with hero image background
2. Scroll down to 'what we do' section with 3 bullet points and icons
3. Scroll down to 'how to use this site' section with 3 bullet points (1,2,3) and instructions
4. Are you a venue? instructions about how to talk to us about listing. And link to the 'how to list' page.

To the left we would want a burger menu with dropdown nav and links

• Design the template for the 'venue listings' pages
o We want to list venues by towns or cities and have one page dedicated for each. We would create each page from the template you provide.
o When the user clicks on any particular venue it clicks through to the individual venue page
o This page should have a map with pins for each listed venue

Here are some examples of the listings pages that we like and why:

http://www.trelbo.com/
What we like about it: Strong blocks and font. Nice hover feature changing the colour and introducing the click through arrow on the right bottom corner

http://www.roomtorrent.co.nz/
What we like about it: Don’t like the colours or design but like the practicality of the search box and the 3 column listings when you select a search criteria. This is a familiar format and maybe easier for the user to understand and navigate around.

http://www.harbourtix.co.nz/venues
What we like about it: Like the simplicity of this page but our listings would need a little more info beneath each one. The hover function is annoying!

• Design the template for the individual venue pages.
• Include a search function across the full site so that users can choose to search for venues in different towns or cities.
• Design the booking form pages for the individual venues (we have working examples of our existing ones)

• Design the payment page and thank you page for those who complete the booking form online. (We will be offering the option on our site to pay by credit card into our coinvale account) We have working examples of our current thank you and payment page although the payment page is not live on our current site.

------------------------------------------------------------------------------------

TECHNICAL
• Pages need to be created in html and css. Some php pages, as required for payment pages. And some javascript for all pages.

• Templates will need to be in dwt format, as we need to be able to upload to Dreamweaver CC and create new pages from the templates for new venues as and when necessary.

• Pages should be responsive for browsing across PC’s Laptops, ipads, phones and other devices.

• Website will be hosted on a Linux server when ready to go live.

A) We can provide existing website files if these help with the design and build process of the new site.
B) We plan to build additional features for the site, as a second phase project. This would include client login areas and electronic confirmations of bookings and online updating of booking forms.

• See the brief provided. Successful designer/developer must be able to supply files in html, css, php (if required) and include javascript coding where necessary. We will be hosting these files and managing the site using Dreamweaver CC so full accessibility to the files is important.
• Notes have been added to the brief. Please read and ask questions if not clear.
• We are not looking for a site to be built using an open source platform. The files provided must be able to be uploaded to our own server for our own management after the end of the project.

```html
<!DOCTYPE html>
<html lang="en">
<head>
<meta charset="utf-8">
<title>Halvoro – Venue Hire for Conferences and Events</title>
<link rel="stylesheet" href="https://fonts.googleapis.com/css2?family=Questrial&family=Open+Sans:wght@400;600&display=swap">
<style>
:root{
  --yellow:#f2c318;
  --ink:#231f20;
  --grey:#7a7a7a;
  --light:#9a9a9a;
  --white:#ffffff;
  --dark-band:#2b2628;
  --footer:#2c3440;
}
*{margin:0;padding:0;box-sizing:border-box}
html,body{width:1200px;height:2590px;overflow:hidden;background:var(--white)}
body{position:relative;font-family:"Open Sans",Arial,sans-serif;color:var(--ink)}
.abs{position:absolute}
.heading{font-family:"Questrial","Century Gothic",sans-serif;font-weight:400;text-align:center;letter-spacing:1px}
.heading .muted{color:var(--grey)}
.center{left:0;width:1200px;text-align:center}

/* hero */
.hero{top:0;left:0;width:1200px;height:594px;overflow:hidden}
.hero-photo{position:absolute;inset:0;background:
  radial-gradient(ellipse at 50% 70%,rgba(210,205,200,.55),transparent 60%),
  linear-gradient(180deg,#3a2a1e 0%,#5a4434 35%,#8d8178 65%,#c9c5c2 100%)}
.hero-shade{position:absolute;inset:0;background:rgba(20,14,10,.35)}
.burger{left:62px;top:68px;width:26px}
.burger span{display:block;height:3px;background:var(--white);margin-bottom:5px}
.brand{top:30px;left:0;width:1200px;text-align:center;color:var(--white)}
.brand-mark{width:74px;height:74px;border:2px solid var(--white);border-radius:50%;margin:0 auto 12px}
.brand-name{font-family:"Questrial",sans-serif;font-size:34px;letter-spacing:2px;line-height:1}
.hero-title{top:322px;font-family:"Questrial",sans-serif;font-size:36px;color:var(--white)}
.hero-title .accent{color:var(--yellow)}
.dots{top:557px;left:525px;display:flex;gap:20px;align-items:center}
.dots i{width:10px;height:10px;border-radius:50%;background:var(--white)}
.dots i.active{width:24px;height:12px;background:none;border:2px solid var(--yellow)}

/* what we do */
.what-title{top:642px;font-size:38px}
.intro{top:706px;left:120px;width:960px;font-size:13px;line-height:24px;color:var(--light);text-align:center}
.feature{top:825px;width:340px;text-align:center}
.feature svg{display:block;margin:0 auto}
.feature h3{font-family:"Questrial",sans-serif;font-weight:400;font-size:23px;margin-top:30px;color:var(--ink)}
.feature p{font-size:13px;line-height:22px;color:var(--grey);margin-top:16px}

/* how to use */
.how{top:1145px;left:0;width:1200px;height:514px;background:linear-gradient(180deg,#3b3236,#2b2628 50%,#3a2e33)}
.how-title{top:1180px;font-size:38px;color:var(--white)}
.how-title .muted{color:#b8b3b4}
.step{top:1260px;width:322px;text-align:center}
.step-photo{height:208px}
.step-badge{width:92px;height:92px;border-radius:50%;background:var(--yellow);margin:-46px auto 0;font-family:"Questrial",sans-serif;font-size:20px;line-height:92px;color:var(--ink);position:relative}
.step h3{font-family:"Questrial",sans-serif;font-weight:400;font-size:24px;color:var(--yellow);margin-top:14px}
.step p{font-size:13px;line-height:22px;color:#8f888a;margin-top:8px;padding:0 18px}
.step-arrow{top:1470px}

/* venue */
.venue-title{top:1708px;font-size:38px}
.venue-copy{top:1782px;left:110px;width:980px;font-size:13px;line-height:22px;color:#555;text-align:center}
.venue-copy p{margin-bottom:22px}
.btn{top:2015px;left:496px;width:208px;height:56px;border-radius:28px;background:var(--ink);color:var(--yellow);font-size:13px;font-weight:600;display:flex;align-items:center;justify-content:center;gap:12px}

/* contact band */
.contact{top:2138px;left:0;width:1200px;height:129px;background:var(--yellow);display:flex}
.contact-item{flex:1;display:flex;align-items:center;justify-content:center;gap:14px;font-family:"Questrial",sans-serif;font-size:19px;color:var(--white);border-right:1px solid rgba(0,0,0,.1);margin:25px 0}
.contact-item:last-child{border:none;font-size:16px;line-height:20px}

/* footer */
.footer{top:2267px;left:0;width:1200px;height:323px}
.footer-photo{position:absolute;inset:0;background:linear-gradient(180deg,#2f3945,#3b4652 55%,#2a3540)}
.footer-shade{position:absolute;inset:0;background:rgba(20,24,32,.45)}
.mail-tab{top:2267px;left:553px;width:94px;height:42px;border-radius:0 0 47px 47px;background:#3a3a3c;display:flex;align-items:center;justify-content:center}
.footer-brand{top:2345px;left:130px;width:210px;text-align:center;color:var(--white)}
.footer-brand .brand-mark{width:58px;height:58px}
.footer-brand .brand-name{font-size:28px}
.social{top:2470px;left:140px;display:flex;gap:22px}
.social i{width:16px;height:16px;border-radius:50%;background:var(--white)}
.copy{top:2508px;left:128px;font-size:11px;color:var(--white)}
.copy .accent{color:var(--yellow)}
.foot-col{top:2354px;color:var(--white)}
.foot-col h4{font-family:"Questrial",sans-serif;font-weight:400;font-size:18px;letter-spacing:.5px;margin-bottom:22px}
.foot-col h4 .accent{color:var(--yellow)}
.foot-col li{list-style:none;font-size:13px;line-height:25px;color:#e6e6e6}
</style>
</head>
<body>

<header class="abs hero">
  <div class="hero-photo" role="img" aria-label="Photo of an elegant restaurant hall with laid tables under a timber roof"></div>
  <div class="hero-shade"></div>
</header>
<div class="abs burger" aria-label="Menu"><span></span><span></span><span></span></div>
<div class="abs brand">
  <div class="brand-mark"></div>
  <div class="brand-name">HALVORO</div>
</div>
<h1 class="abs center hero-title"><span class="accent">Venue Hire</span> for Conferences and Events</h1>
<div class="abs dots"><i></i><i></i><i class="active"></i><i></i><i></i></div>

<h2 class="abs center heading what-title"><span class="muted">WHAT WE DO</span> FOR YOU</h2>
<p class="abs intro">We are your professional conference and event organisers, providing you with multiple venue options and conference solutions all in one place. Why spend hours searching for venues and contacing each one when we'll do all that for you.</p>

<section class="abs feature" style="left:60px">
  <svg width="120" height="116" viewBox="0 0 120 116" fill="none" stroke="var(--yellow)" stroke-width="5">
    <path d="M60 108 C42 82 30 66 30 46 a30 30 0 0 1 60 0 c0 20-12 36-30 62z"/>
    <circle cx="60" cy="46" r="11"/>
  </svg>
  <h3>Verified venues</h3>
  <p>Search for the perfect space from<br>our 4500+ verified venues.</p>
</section>
<section class="abs feature" style="left:410px">
  <svg width="120" height="116" viewBox="0 0 120 116" fill="none" stroke="var(--yellow)" stroke-width="5">
    <rect x="10" y="20" width="100" height="70" rx="8"/>
    <line x1="10" y1="40" x2="110" y2="40"/>
    <line x1="24" y1="70" x2="50" y2="70"/>
  </svg>
  <h3>Book and pay online</h3>
  <p>Book space easily with a few clicks,<br>pay securely, and get confirmation.</p>
</section>
<section class="abs feature" style="left:778px">
  <svg width="120" height="116" viewBox="0 0 120 116" fill="none" stroke="var(--yellow)" stroke-width="5">
    <circle cx="60" cy="58" r="40"/>
    <path d="M60 34 v26 h18" stroke-linecap="round"/>
  </svg>
  <h3>At your service, 24/7</h3>
  <p>Our customer support team is here to<br>make sure you are well looked after.</p>
</section>

<section class="abs how" role="img" aria-label="Dim background photo of a floral event setting"></section>
<h2 class="abs center heading how-title"><span class="muted">HOW TO USE</span> THIS SITE</h2>

<div class="abs step" style="left:79px">
  <div class="step-photo" role="img" aria-label="Photo of a hand holding a phone showing a map" style="background:linear-gradient(135deg,#c9b8a8,#e8e2dc 55%,#9fb0a8)"></div>
  <div class="step-badge">STEP 1</div>
  <h3>Finding a venue</h3>
  <p>Lorem ipsum dolor sit amet, consectetur adipisc elit. Mauris ac blandit augue.</p>
</div>
<div class="abs step" style="left:439px">
  <div class="step-photo" role="img" aria-label="Photo of hands writing in a notebook beside a laptop" style="background:linear-gradient(135deg,#7fb0c8,#e9eef0 55%,#b9c6cc)"></div>
  <div class="step-badge">STEP 2</div>
  <h3>Listing a venue</h3>
  <p>Lorem ipsum dolor sit amet, consectetur adipisc elit. Mauris ac blandit augue.</p>
</div>
<div class="abs step" style="left:799px">
  <div class="step-photo" role="img" aria-label="Photo of a banquet table with folded napkins and glasses" style="background:linear-gradient(135deg,#5a3a1e,#d7b98a 50%,#8a6a48)"></div>
  <div class="step-badge">STEP 3</div>
  <h3>Managing your venue</h3>
  <p>Lorem ipsum dolor sit amet, consectetur adipisc elit. Mauris ac blandit augue.</p>
</div>
<svg class="abs step-arrow" style="left:286px" width="668" height="22" viewBox="0 0 668 22" fill="none" stroke="var(--yellow)" stroke-width="2">
  <line x1="0" y1="11" x2="124" y2="11"/><path d="M114 2 l12 9 -12 9"/>
  <line x1="360" y1="11" x2="484" y2="11"/><path d="M474 2 l12 9 -12 9"/>
</svg>

<h2 class="abs center heading venue-title"><span class="muted">ARE YOU A</span> VENUE?</h2>
<div class="abs venue-copy">
  <p>The venues we work with are private, secure and of the highest quality. We aim to ensure that the range of properties and meeting rooms in the portfolio always have a point of difference from each other so that you have maximum flexibility and options to suit your needs, whatever they are. Some spaces are small and intimate for groups of up to 12 people. Others are large and spacious for conference groups of up to 150 or parties and functions of up to 300.</p>
  <p>Our hotel partners provide full service conference solutions and 4 and 5 star accommodation for all your out of town guests and we work with high quality caterers to provide delicious menus to suit your event needs.</p>
  <p>Even if you don't require a full day, please contact us with your request as we can provide flexible solutions subject to availability.</p>
</div>
<a class="abs btn">HOW TO LIST
  <svg width="14" height="12" viewBox="0 0 14 12" fill="var(--yellow)"><path d="M0 5h9V1l5 5-5 5V7H0z"/></svg>
</a>

<section class="abs contact">
  <div class="contact-item">
    <svg width="18" height="30" viewBox="0 0 18 30" fill="none" stroke="#fff" stroke-width="2.5"><rect x="2" y="2" width="14" height="26" rx="3"/><line x1="7" y1="23" x2="11" y2="23"/></svg>
    1-800-555-0142
  </div>
  <div class="contact-item">
    <svg width="28" height="20" viewBox="0 0 28 20"><rect width="28" height="20" rx="2" fill="#fff"/><path d="M1 2l13 10L27 2" fill="none" stroke="var(--yellow)" stroke-width="2.5"/></svg>
    info@halvoro.org
  </div>
  <div class="contact-item">
    <svg width="20" height="28" viewBox="0 0 20 28"><path d="M10 0a10 10 0 0 1 10 10c0 7-10 18-10 18S0 17 0 10A10 10 0 0 1 10 0z" fill="#fff"/><circle cx="10" cy="10" r="4" fill="var(--yellow)"/></svg>
    <span>Lorem Ipsum, 10 The Avenue<br>Another Street, Canada</span>
  </div>
</section>

<footer class="abs footer">
  <div class="footer-photo" role="img" aria-label="Photo of an outdoor terrace with chairs beside an infinity pool at dusk"></div>
  <div class="footer-shade"></div>
</footer>
<div class="abs mail-tab">
  <svg width="22" height="16" viewBox="0 0 22 16" fill="none" stroke="var(--yellow)" stroke-width="2"><rect x="1" y="1" width="20" height="14" rx="1"/><path d="M1 2l10 7 10-7"/></svg>
</div>
<div class="abs footer-brand">
  <div class="brand-mark"></div>
  <div class="brand-name">HALVORO</div>
</div>
<div class="abs social" aria-label="Social links"><i></i><i></i><i></i><i></i><i></i></div>
<p class="abs copy"><span class="accent">© 2016 Copyrights.</span> All Rights Reserved</p>

<nav class="abs foot-col" style="left:486px">
  <h4>MAIN <span class="accent">MENU</span></h4>
  <ul><li>Search</li><li>About Us</li><li>Blog</li><li>How to list</li><li>Contact us</li></ul>
</nav>
<nav class="abs foot-col" style="left:690px">
  <h4>QUICK <span class="accent">LINKS</span></h4>
  <ul><li>How it works</li><li>Plinq for venues</li><li>Guide for venues</li><li>Careers</li><li>Support</li></ul>
</nav>
<nav class="abs foot-col" style="left:932px">
  <h4>SITE <span class="accent">POLICIES</span></h4>
  <ul><li>SMS Terms of Service</li><li>Refund Policy</li><li>Earnings Disclaimer</li><li>Privacy Policy</li></ul>
</nav>

</body>
</html>
```